Marlow Vantage - Health, Wellness, Fitness Consultants

Marlow Vantage are Marlow Vantage are leading consultants to the Health, Wellness and Fitness industry​​, with over 25 years experience working with some of the biggest global worldwide brands from equipment providers and facility operators to mass participation events and obstacle course races. Marlow Vantage is a multi disciplined business specialising in helping brands grow through insight, strategy creation and valuable sector collaboration, We are the official exclusive distributors of Kinfor Rig bodyweight training products for the UK and Ireland, Official Partners of Obstacle Course Race and Adventure Racing Brindle Dash & Cobalt Trek Tour - I would like a black background card, 1 side Marlow Vantage logo only other side Official, Exclusive, Distributors and Partners in the UK & Ireland. Then list Brindle Dash, Kinfor Rig, Cobalt Trek Tour contact details at very bottom Founder / Director - Perry Dunmore
Mobile - +44(0)7900123456
E - Mail - perry.dunmore@marlowvantage.example
Web - www.marlowvantage.example
Skype - marlowvantage

```html
<!DOCTYPE html>
<html lang="en">
<head>
<meta charset="utf-8">
<title>Marlow Vantage – Business Card</title>
<link rel="stylesheet" href="https://fonts.googleapis.com/css2?family=Source+Sans+3:wght@400;600;700&family=Tinos&display=swap">
<style>
  :root {
    --olive: #6a7a3a;
    --olive-light: #8f9a5e;
    --ink: #111111;
    --card-black: #0b0b0b;
    --paper: #ffffff;
    --faint: #2a2a2a;
    --gold: #b8a36a;
    --orange: #f07a2a;
    --blue: #2e4fd6;
  }
  html, body {
    margin: 0;
    width: 1200px;
    height: 900px;
    overflow: hidden;
  }
  body {
    position: relative;
    background: linear-gradient(135deg, #151515 0%, #6a6a6a 45%, #e4e4e4 100%);
    font-family: "Source Sans 3", "Helvetica Neue", Arial, sans-serif;
  }
  .card {
    position: absolute;
    top: 184px;
    height: 490px;
    border-radius: 12px;
    overflow: hidden;
    box-shadow: 0 4px 14px rgba(0,0,0,0.35);
  }
  .card--front { left: 299px; width: 301px; background: var(--paper); }
  .card--back { left: 645px; width: 304px; background: var(--card-black); }

  .front-top {
    position: absolute; inset: 0 0 156px 0;
    background: linear-gradient(180deg, #f6f6f3 0%, #ffffff 60%, #f3f3f1 100%);
    text-align: center;
    color: var(--ink);
  }
  .holder-name {
    margin: 76px 0 0;
    font-size: 25px; font-weight: 700; color: var(--olive);
    line-height: 1;
  }
  .holder-role { margin: 6px 0 0; font-size: 15px; line-height: 1.2; }
  .rule { width: 160px; height: 1px; background: var(--olive-light); margin: 11px auto 9px; }
  .contact { margin: 0; font-size: 14.5px; line-height: 20px; white-space: nowrap; }
  .tagline {
    margin: 33px 0 0;
    font-size: 15px; font-weight: 600; color: var(--olive); line-height: 20px;
  }
  .front-band {
    position: absolute; left: 0; right: 0; top: 330px; height: 4px;
    background: var(--olive-light);
  }
  .front-bottom {
    position: absolute; left: 0; right: 0; bottom: 0; height: 156px;
    background: linear-gradient(180deg, #141414 0%, #000 100%);
  }
  .services-faint {
    position: absolute; top: 10px; left: 0; right: 0;
    text-align: center; white-space: nowrap;
    font-family: "Tinos", "Times New Roman", serif;
    font-size: 15px; color: var(--faint);
  }
  .partner-slot {
    position: absolute; text-align: center;
  }
  .partner-slot--left { left: 6px; width: 150px; top: 44px; }
  .partner-slot--right { left: 156px; width: 140px; top: 0; height: 156px; }
  .partner-mark {
    display: block; margin: 0 auto;
    width: 46px; height: 46px; border-radius: 50%; border: 2px solid #fff;
  }
  .partner {
    margin: 0; font-weight: 700; white-space: nowrap; line-height: 1;
  }
  .partner--trek { margin-top: 10px; font-size: 17px; color: var(--orange); }
  .partner--dash {
    position: absolute; left: 0; right: 0; top: 42px;
    font-size: 15px; color: #fff;
  }
  .partner--rig {
    position: absolute; left: 0; right: 0; top: 108px;
    font-size: 19px; color: var(--blue);
  }

  .back-mark {
    position: absolute; left: 0; right: 0; top: 250px;
    text-align: center;
  }
  .back-brand {
    margin: 0;
    font-family: "Tinos", "Times New Roman", serif;
    font-size: 34px; color: var(--gold); line-height: 1;
  }
  .back-services {
    margin: 16px 0 0;
    font-family: "Tinos", "Times New Roman", serif;
    font-size: 10px; color: var(--gold);
  }
</style>
</head>
<body>
  <section class="card card--front" aria-label="Card front">
    <div class="front-top">
      <h1 class="holder-name">Perry Dunmore</h1>
      <p class="holder-role">Founder / Director</p>
      <div class="rule"></div>
      <p class="contact">M: +44(0)7900123456</p>
      <p class="contact">E: perry.dunmore@marlowvantage.example</p>
      <p class="contact">www.marlowvantage.example</p>
      <p class="contact">Skype - marlowvantage</p>
      <p class="tagline">Official, Exclusive, Distributors<br>and Partners in the UK &amp; Ireland.</p>
    </div>
    <div class="front-band"></div>
    <div class="front-bottom">
      <span class="services-faint">Health | Wellness | Fitness | Consultants</span>
      <div class="partner-slot partner-slot--left">
        <span class="partner-mark"></span>
        <p class="partner partner--trek">Cobalt Trek Tour</p>
      </div>
      <div class="partner-slot partner-slot--right">
        <p class="partner partner--dash">Brindle Dash</p>
        <p class="partner partner--rig">Kinfor Rig</p>
      </div>
    </div>
  </section>

  <section class="card card--back" aria-label="Card back">
    <div class="back-mark">
      <p class="back-brand">Marlow Vantage</p>
      <p class="back-services">Health | Wellness | Fitness | Consultants</p>
    </div>
  </section>
</body>
</html>
```